Graphic Design Project adhesive label

We are a handkerchief wholesaler and require an adhesive sticker to stick on top left side single cello bag 170mm x 170mm. Then to run down the back of back noting our details. Flat and folded inside bag is a floral and or paisley ladies handkerchief.
Sticker approx 30cm wide 90mm long but folded at 45mm. 45mm down the front of bag and 45mm going down back of bag. Changed cm to mm.

Wording for Front sticker:

Marlowe Cloth
handkerchief
by .Tennick.

Back of sticker:

Made from imported English Marlowe cloth
100% cotton traditional hemstitch finish
www.tennick-example.com

Hi - Sorry made a mistake with measurements should be 170 mm not 170cm. Same with sticker mm's.                                     

Reason: Extending deadline as will be away until wednesday 2/5/13

Reason: Have been away and have not had a chance to consider designs, thanks for your patience. T

Target Market(s)

mature generally

Industry/Entity Type

Floral

Requirements
Must have
• prefer a lighter background
Nice to have
• Apart from wording some sort of back ground design, colour or symbol

```html
<!DOCTYPE html>
<html lang="en">
<head>
<meta charset="utf-8">
<title>Marlowe Cloth Handkerchief – Label</title>
<link href="https://fonts.googleapis.com/css2?family=EB+Garamond:wght@400;500&display=swap" rel="stylesheet">
<style>
  :root {
    --page: #ffffff;
    --ink: #4a3a30;
    --text: #2e2622;
    --panel-edge: #e4e2e0;
    --band: #6b5a4e;
    --band-light: #d9d2cc;
    --petal: #ecc3bb;
    --leaf: #c6cfae;
    --cream: #f7f1ea;
  }
  * { box-sizing: border-box; margin: 0; padding: 0; }
  html, body {
    width: 1200px; height: 655px; overflow: hidden;
    background: var(--page);
  }
  .canvas {
    position: relative; width: 1200px; height: 655px;
    font-family: "EB Garamond", Garamond, serif;
    color: var(--text);
  }
  .side-label {
    position: absolute; top: 14px; width: 540px;
    text-align: center; font-size: 53px; font-weight: 400;
    color: var(--ink); line-height: 1;
  }
  .side-label--front { left: 48px; }
  .side-label--back { left: 608px; }

  .panel {
    position: absolute; top: 84px; width: 540px; height: 540px;
    border: 1px solid var(--panel-edge); background: var(--page);
    overflow: hidden;
  }
  .panel--front { left: 48px; }
  .panel--back { left: 608px; }

  .ornament-band {
    position: absolute; left: 0; width: 100%; height: 30px;
    background: linear-gradient(var(--band) 0 3px, var(--band-light) 3px 27px, var(--band) 27px 30px);
  }
  .panel--front .ornament-band { bottom: 0; }
  .panel--back .ornament-band { top: 0; }

  .floral {
    position: absolute;
    background:
      radial-gradient(circle at 60% 40%, var(--petal) 0 18%, transparent 40%),
      radial-gradient(circle at 30% 70%, var(--leaf) 0 15%, transparent 40%),
      var(--cream);
  }
  .panel--front .floral { left: 0; top: 0; width: 295px; height: 312px; border-bottom-right-radius: 60%; }
  .panel--back .floral { right: 0; bottom: 0; width: 290px; height: 312px; border-top-left-radius: 60%; }

  .product-title {
    position: absolute; left: 236px; width: 270px; top: 320px;
    text-align: center;
  }
  .product-title__name {
    font-size: 36px; line-height: 42px; font-weight: 400;
  }
  .product-title__maker {
    font-size: 23px; margin-top: 8px;
  }

  .product-details {
    position: absolute; top: 76px; left: 0; width: 100%;
    text-align: center;
  }
  .product-details__line { font-size: 18px; line-height: 27px; }
  .product-details__web { font-size: 21px; margin-top: 19px; }
</style>
</head>
<body>
<main class="canvas">
  <h2 class="side-label side-label--front">Front</h2>
  <h2 class="side-label side-label--back">Back</h2>

  <section class="panel panel--front">
    <div class="floral" role="img" aria-label="Floral illustration of pink blossoms, green leaves and brown scrolling vines"></div>
    <div class="product-title">
      <h1 class="product-title__name">Marlowe Cloth<br>Handkerchief</h1>
      <p class="product-title__maker">by. Tennick</p>
    </div>
    <div class="ornament-band" role="img" aria-label="Decorative brown scrollwork border"></div>
  </section>

  <section class="panel panel--back">
    <div class="ornament-band" role="img" aria-label="Decorative brown scrollwork border"></div>
    <div class="product-details">
      <p class="product-details__line">Made from imported English Marlowe cloth</p>
      <p class="product-details__line">100% cotton traditional hemstitch finish</p>
      <p class="product-details__web">www.tennick-example.com</p>
    </div>
    <div class="floral" role="img" aria-label="Floral illustration of pink blossoms, green leaves and brown scrolling vines"></div>
  </section>
</main>
</body>
</html>
```